Financial Service Company Need Business Card Design

This is a new startup company, first of its kind to offer this service. We facilitate the movement of deposit funds electronically between home buyers and real estate brokerages.Our customers are DOMIVANS®, real estate brokerages, and home buyers, we identify ourselves as a financial/technology company.
Not looking for anything too flashy. Just a clean design that shows the logo, contact info, etc. Company colors can be seen on attached logo, and 'coming soon page'
www.quorvanta.ca

```html
<!DOCTYPE html>
<html lang="en">
<head>
<meta charset="utf-8">
<title>Quorvanta Business Card</title>
<link href="https://fonts.googleapis.com/css2?family=Montserrat:wght@600;700&family=Arimo:wght@400;700&family=Tinos&display=swap" rel="stylesheet">
<style>
  :root {
    --orange: #e8582a;
    --orange-soft: #ee6a3c;
    --slate: #5f6062;
    --ink: #6b6b6b;
    --paper: #ffffff;
    --backdrop: #ecebe8;
  }
  * { box-sizing: border-box; margin: 0; padding: 0; }
  html, body {
    width: 1200px; height: 1000px; overflow: hidden;
    background: var(--backdrop);
  }
  .sheet { position: relative; width: 1200px; height: 1000px; }
  .card {
    position: absolute; left: 250px; width: 700px; height: 400px;
    box-shadow: 0 6px 20px rgba(0,0,0,.12);
  }
  .card-front {
    top: 70px; background: var(--orange);
    display: flex; align-items: center; justify-content: center;
  }
  .front-name {
    font-family: "Montserrat", sans-serif; font-weight: 700;
    font-size: 92px; color: var(--slate); letter-spacing: -1px;
  }
  .card-back { top: 530px; background: var(--paper); display: flex; }
  .brand-side {
    width: 400px; display: flex; flex-direction: column;
    align-items: center; justify-content: center;
  }
  .brand-row { display: flex; align-items: center; gap: 14px; }
  .brand-mark { width: 22px; height: 22px; background: var(--orange); }
  .brand-name {
    font-family: "Montserrat", sans-serif; font-weight: 700;
    font-size: 52px; color: var(--slate); letter-spacing: -.5px;
  }
  .brand-web {
    margin-top: 10px; font-family: "Arimo", sans-serif;
    font-size: 17px; letter-spacing: 2px; color: var(--ink);
  }
  .divider { width: 1px; margin: 48px 0; background: var(--orange-soft); }
  .contact-side {
    flex: 1; padding: 50px 0 0 40px;
    font-family: "Arimo", sans-serif; color: var(--ink);
  }
  .person-name { font-size: 27px; font-weight: 700; }
  .person-first { color: var(--orange); }
  .person-last { color: var(--slate); }
  .person-role { margin-top: 4px; font-size: 14px; letter-spacing: 5px; color: var(--slate); }
  .contact-list { list-style: none; margin-top: 28px; }
  .contact-item {
    display: flex; align-items: flex-start; gap: 16px;
    font-size: 18px; line-height: 24px; margin-bottom: 8px;
  }
  .contact-item.address { margin-top: 42px; }
  .contact-item .serif { font-family: "Tinos", serif; font-size: 20px; }
  .contact-icon { width: 16px; height: 16px; flex: none; margin-top: 4px; fill: var(--orange); }
</style>
</head>
<body>
<main class="sheet">
  <section class="card card-front">
    <div class="front-name">Quorvanta</div>
  </section>

  <section class="card card-back">
    <div class="brand-side">
      <div class="brand-row">
        <span class="brand-mark"></span>
        <span class="brand-name">Quorvanta</span>
      </div>
      <div class="brand-web">www.quorvanta.ca</div>
    </div>
    <div class="divider"></div>
    <div class="contact-side">
      <div class="person-name"><span class="person-first">Lena</span><span class="person-last">Marsh</span></div>
      <div class="person-role">Designer</div>
      <ul class="contact-list">
        <li class="contact-item">
          <svg class="contact-icon" viewBox="0 0 24 24"><path d="M6.6 10.8a15 15 0 0 0 6.6 6.6l2.2-2.2c.3-.3.7-.4 1-.2 1.1.4 2.3.6 3.6.6.6 0 1 .4 1 1V20c0 .6-.4 1-1 1A17 17 0 0 1 3 4c0-.6.4-1 1-1h3.5c.6 0 1 .4 1 1 0 1.3.2 2.5.6 3.6.1.3 0 .7-.2 1z"/></svg>
          <span class="serif">604-555-0142</span>
        </li>
        <li class="contact-item">
          <svg class="contact-icon" viewBox="0 0 24 24"><path d="M2 5h20v14H2z"/><path d="M3 6l9 7 9-7" fill="none" stroke="#fff" stroke-width="2"/></svg>
          <span>lena@quorvanta.ca</span>
        </li>
        <li class="contact-item address">
          <svg class="contact-icon" viewBox="0 0 24 24"><path d="M12 2a7 7 0 0 0-7 7c0 5 7 13 7 13s7-8 7-13a7 7 0 0 0-7-7zm0 9.5A2.5 2.5 0 1 1 12 6.5a2.5 2.5 0 0 1 0 5z"/></svg>
          <span class="serif">48 Harbour Lane,<br>Vancouver BC</span>
        </li>
      </ul>
    </div>
  </section>
</main>
</body>
</html>
```